Modern Design Business Card industrial maintenance company

Business card design for Company named Brookvale Equipment Services

Target Market(s)

Industrial

Industry/Entity Type

Maintenance and repair

Contact Information for Business Card

Place holder for address, office phone, mobile number and email

Requirements
Must have
• Clean modern look
Nice to have
• N/a

```html
<!DOCTYPE html>
<html lang="en">
<head>
<meta charset="utf-8">
<title>Brookvale Equipment Services – Business Card</title>
<link href="https://fonts.googleapis.com/css2?family=Lato:wght@400;700;900&display=swap" rel="stylesheet">
<style>
  :root {
    --backdrop: #8e8d8e;
    --paper: #f4f4f6;
    --ink: #0b0c0e;
    --ink-soft: #4a4a4e;
    --band-grey: #6b6b6e;
    --white: #ffffff;
  }
  * { box-sizing: border-box; margin: 0; padding: 0; }
  html, body {
    width: 1200px; height: 1020px; overflow: hidden;
    background: var(--backdrop);
    font-family: "Lato", sans-serif;
  }
  .card {
    position: absolute;
    width: 700px; height: 400px;
    left: 250px;
    box-shadow: 0 18px 40px rgba(0,0,0,0.35);
    overflow: hidden;
  }
  .card--front { top: 70px; background: var(--paper); }
  .card--back { top: 550px; background: var(--ink); }

  /* front */
  .brand {
    position: absolute;
    display: flex; align-items: center; gap: 12px;
  }
  .brand__mark {
    border-radius: 50%;
    border: 4px solid var(--ink);
    flex: none;
  }
  .brand__name {
    font-weight: 700;
    text-transform: uppercase;
    color: var(--ink);
    line-height: 1.15;
    letter-spacing: 0.04em;
  }
  .card--front .brand {
    left: 40px; top: 110px; width: 320px;
    flex-direction: column; gap: 14px; text-align: center;
  }
  .card--front .brand__mark { width: 84px; height: 84px; }
  .card--front .brand__name { font-size: 21px; }

  .divider {
    position: absolute; left: 368px; top: 70px;
    width: 2px; height: 210px; background: var(--ink);
  }
  .contact { position: absolute; left: 400px; top: 62px; color: var(--ink-soft); }
  .contact__name { font-size: 30px; font-weight: 900; color: var(--ink); letter-spacing: 0.01em; }
  .contact__role { font-size: 17px; margin-top: 2px; }
  .contact__address { font-size: 17px; margin-top: 12px; line-height: 1.2; }
  .contact__list { list-style: none; margin-top: 8px; font-size: 17px; }
  .contact__list li { display: flex; align-items: center; gap: 12px; height: 26px; }
  .contact__list svg { width: 16px; height: 16px; flex: none; }

  .band { position: absolute; }
  .band--main { left: 0; top: 296px; width: 560px; height: 24px; background: var(--ink); }
  .band--grey { left: 596px; top: 272px; width: 104px; height: 16px; background: var(--band-grey); }
  .band--base { left: 0; top: 340px; width: 700px; height: 26px; background: var(--ink); }
  .band__badge {
    position: absolute; left: 548px; top: 262px;
    width: 56px; height: 56px; border-radius: 50%;
    background: var(--paper); border: 3px solid var(--ink);
  }

  /* back */
  .card--back .brand { left: 140px; top: 150px; }
  .card--back .brand__mark { width: 100px; height: 100px; border-color: var(--white); }
  .card--back .brand__name { color: var(--white); font-size: 30px; }
</style>
</head>
<body>
  <section class="card card--front">
    <div class="brand">
      <span class="brand__mark"></span>
      <span class="brand__name">Brookvale<br>Equipment Services</span>
    </div>
    <span class="divider"></span>
    <div class="contact">
      <h1 class="contact__name">DANIEL REYES</h1>
      <p class="contact__role">Founder &amp; CEO</p>
      <p class="contact__address">1234 First Line Address<br>5678 Second Line Address</p>
      <ul class="contact__list">
        <li><svg viewBox="0 0 16 16"><path d="M4 1l3 3-1.5 2a8 8 0 0 0 4.5 4.5L12 9l3 3-2 2.5C7 14 2 9 1.5 3z" fill="var(--ink)"/></svg>222-4444-8888</li>
        <li><svg viewBox="0 0 16 16"><rect x="1" y="3" width="14" height="10" fill="var(--ink)"/><path d="M1 3l7 6 7-6" stroke="var(--paper)" stroke-width="1.4" fill="none"/></svg>info@yourmail.com</li>
        <li><svg viewBox="0 0 16 16"><circle cx="8" cy="8" r="6.5" fill="none" stroke="var(--ink)" stroke-width="1.5"/><path d="M1.5 8h13M8 1.5c-3 3.5-3 9.5 0 13M8 1.5c3 3.5 3 9.5 0 13" stroke="var(--ink)" stroke-width="1.2" fill="none"/></svg>www.yourwebsite.com</li>
      </ul>
    </div>
    <span class="band band--grey"></span>
    <span class="band band--main"></span>
    <span class="band__badge"></span>
    <span class="band band--base"></span>
  </section>

  <section class="card card--back">
    <div class="brand">
      <span class="brand__mark"></span>
      <span class="brand__name">Brookvale<br>Equipment Services</span>
    </div>
  </section>
</body>
</html>
```